Business Card Design using new logo

As much as we'd like to think that treating everyone equally is the best strategy for fairness, the reality is that the differences in the lives of women and men have to be taken into account to ensure that organizations, programs, services, and yes, even public policy treat women and men in ways that achieve gender equity.

That's where ParityLumen - fairness metrics insight comes in. Using the data-driven tools of gender analysis, our organization can help anyone determine if gender equity is being achieved - in businesses and organizations, in the planning and implementation of programs and services, and in the development and enforcement of public policy.
Updates

Apologies for the delay - have not had time to finalize the decision.  Should be early this week - probably Tuesday.

Industry/Entity Type

Business

Requirements
Must have
• New Logo for ParityLumen
• Logo plus words "Fairness Metrics Insight"

```html
<!DOCTYPE html>
<html lang="en">
<head>
<meta charset="utf-8">
<title>ParityLumen Business Card</title>
<link rel="stylesheet" href="https://fonts.googleapis.com/css2?family=Open+Sans:wght@400;600&display=swap">
<style>
  :root {
    --page-bg: #d9d9d9;
    --card-dark: #231f1e;
    --card-dark-edge: #2f2a28;
    --card-light: #ffffff;
    --accent: #f0881a;
    --ink-dark: #2a2a2a;
    --ink-light: #f2f2f2;
    --ink-muted: #c9c9c9;
    --rule: #6b6561;
  }
  * { box-sizing: border-box; margin: 0; padding: 0; }
  html, body {
    width: 1200px; height: 944px; overflow: hidden;
    background: var(--page-bg);
    font-family: "Open Sans", Verdana, sans-serif;
  }
  .sheet { position: relative; width: 1200px; height: 944px; }
  .card {
    position: absolute; left: 250px; width: 700px; height: 400px;
    border-radius: 26px; overflow: hidden;
    box-shadow: 0 10px 24px rgba(0,0,0,.22);
  }
  .card-front { top: 52px; background: radial-gradient(circle at 60% 40%, var(--card-dark-edge), var(--card-dark) 70%); }
  .card-back { top: 492px; background: var(--card-light); }

  .brand { position: absolute; display: flex; align-items: center; gap: 18px; }
  .brand-dot { width: 62px; height: 62px; border-radius: 50%; background: var(--accent); flex: none; }
  .brand-name { font-weight: 600; font-size: 64px; letter-spacing: -0.5px; line-height: 1; }
  .card-front .brand { left: 84px; top: 126px; }
  .card-front .brand-name { color: var(--ink-light); }
  .tagline {
    position: absolute; left: 246px; top: 252px;
    color: var(--ink-muted); font-size: 24px; letter-spacing: 1.5px;
  }

  .back-art { position: absolute; inset: 0; width: 700px; height: 400px; }
  .card-back .brand { left: 170px; top: 78px; }
  .card-back .brand-dot { width: 52px; height: 52px; }
  .card-back .brand-name { color: var(--ink-dark); font-size: 56px; }

  .person { position: absolute; left: 84px; top: 248px; color: var(--ink-light); }
  .person-name { color: var(--accent); font-size: 22px; font-weight: 600; }
  .person-role { font-size: 17px; margin-top: 2px; }
  .address { display: flex; gap: 10px; margin-top: 18px; font-size: 19px; line-height: 1.3; }
  .divider { position: absolute; left: 362px; top: 250px; width: 1px; height: 120px; background: var(--rule); }
  .contacts { position: absolute; left: 388px; top: 246px; list-style: none; color: var(--ink-light); font-size: 19px; }
  .contacts li { display: flex; align-items: center; gap: 10px; height: 28px; }
  .icon { width: 16px; height: 16px; flex: none; fill: var(--accent); }
</style>
</head>
<body>
<main class="sheet">
  <section class="card card-front" aria-label="Card front">
    <div class="brand">
      <span class="brand-dot"></span>
      <span class="brand-name">ParityLumen</span>
    </div>
    <p class="tagline">Fairness Metrics Insight</p>
  </section>

  <section class="card card-back" aria-label="Card back">
    <svg class="back-art" viewBox="0 0 700 400" aria-hidden="true">
      <path d="M0 196 C 200 246 430 240 700 178 L700 206 C 430 262 200 262 0 222 Z" fill="var(--accent)"/>
      <path d="M0 226 C 200 266 430 266 700 212 L700 400 L0 400 Z" fill="var(--card-dark)"/>
    </svg>
    <div class="brand">
      <span class="brand-dot"></span>
      <span class="brand-name">ParityLumen</span>
    </div>

    <div class="person">
      <p class="person-name">Marcus Vellan</p>
      <p class="person-role">director</p>
      <div class="address">
        <svg class="icon" viewBox="0 0 16 16" aria-hidden="true"><path d="M8 1 L15 8 H13 V15 H10 V10 H6 V15 H3 V8 H1 Z"/></svg>
        <p>1450 Orren Vale Rd<br>Calder, TX 78114</p>
      </div>
    </div>

    <div class="divider"></div>

    <ul class="contacts">
      <li><svg class="icon" viewBox="0 0 16 16" aria-hidden="true"><path d="M4 1 L7 4 L5 6 C6 8 8 10 10 11 L12 9 L15 12 L13 15 C7 15 1 9 1 3 Z"/></svg>555-014-2210</li>
      <li><svg class="icon" viewBox="0 0 16 16" aria-hidden="true"><path d="M4 1 H12 V5 H4 Z M1 6 H15 V12 H12 V15 H4 V12 H1 Z M6 10 V13 H10 V10 Z"/></svg>555-014-2211</li>
      <li><svg class="icon" viewBox="0 0 16 16" aria-hidden="true"><path d="M1 3 H15 V13 H1 Z M2 4 L8 9 L14 4 Z" fill-rule="evenodd"/></svg>info@paritylumen.com</li>
      <li><svg class="icon" viewBox="0 0 16 16" aria-hidden="true"><circle cx="8" cy="8" r="7"/></svg>www.paritylumen.com</li>
    </ul>
  </section>
</main>
</body>
</html>
```